Want to incorporate elements of all these items to make an amazing sign to welcome people to the community. The sign is 6x4 and needs to incorporate the following items:

Welcome to Corwick Meadows

Come visit the PRD sales center at 745 thistledown road
High Speed Fiber Internet
Land financing starting at $299 (No credit checks)
Let us build your dream home!
555-284-7390
We like the gold and black design no teal or blue that was another agents design. Some combination of the current sign all the stuff listed above and then design elements that tie into the truck wrap.

Target Market(s)

People visiting the neighborhood

Industry/Entity Type

real estate and construction

Font styles to use
Serif

Colors

Designer to choose colors to be used in the design.

Requirements
Must have
• PRD Home Builders Welcomes you to Corwick Meadows, Let us build your dream home, Phone number, Land financing starting at $299 NO credit checks

```html
<!DOCTYPE html>
<html lang="en">
<head>
<meta charset="UTF-8">
<title>Welcome to Corwick Meadows</title>
<link href="https://fonts.googleapis.com/css2?family=Cinzel:wght@600;700;800&family=EB+Garamond:wght@600;700&family=Montserrat:wght@400;500;700&display=swap" rel="stylesheet">
<style>
  :root {
    --ink: #000000;
    --gold-light: #f8dd8e;
    --gold: #e3b45d;
    --gold-deep: #a8702f;
    --gold-shine: #fbe7a6;
    --gold-text: linear-gradient(180deg, var(--gold-shine) 0%, var(--gold) 45%, var(--gold-deep) 80%, var(--gold-light) 100%);
    --gold-side: linear-gradient(90deg, var(--gold-deep) 0%, var(--gold-light) 40%, var(--gold) 70%, var(--gold-deep) 100%);
  }
  html, body { margin: 0; padding: 0; overflow: hidden; background: var(--ink); }
  .sign {
    position: relative;
    width: 1200px; height: 800px;
    background: var(--ink);
    overflow: hidden;
  }
  .frame { position: absolute; inset: 0; }
  .flourish {
    position: absolute;
    width: 190px; height: 190px;
  }
  .flourish--tl { left: 0; top: 0; background: radial-gradient(circle at 22% 22%, rgba(227,180,93,.45), rgba(227,180,93,0) 65%); }
  .flourish--tr { right: 0; top: 0; background: radial-gradient(circle at 78% 22%, rgba(227,180,93,.45), rgba(227,180,93,0) 65%); }
  .flourish--bl { left: 0; bottom: 0; background: radial-gradient(circle at 22% 78%, rgba(227,180,93,.45), rgba(227,180,93,0) 65%); }
  .flourish--br { right: 0; bottom: 0; background: radial-gradient(circle at 78% 78%, rgba(227,180,93,.45), rgba(227,180,93,0) 65%); }

  .gold {
    background: var(--gold-text);
    -webkit-background-clip: text;
    background-clip: text;
    color: transparent;
  }
  .line { position: absolute; left: 0; right: 0; margin: 0; text-align: center; white-space: nowrap; }

  .welcome {
    top: 34px;
    font-family: "Cinzel", serif; font-weight: 700;
    font-size: 38px; letter-spacing: 2px;
  }
  .welcome span { background-color: transparent; padding: 0 18px; }
  .welcome-mask {
    position: absolute; left: 440px; top: 14px; width: 320px; height: 20px; background: var(--ink);
  }
  .community {
    top: 82px;
    font-family: "Cinzel", serif; font-weight: 800;
    font-size: 92px; letter-spacing: 1px; line-height: 1.2;
  }
  .rule {
    position: absolute; left: 230px; top: 211px; width: 740px; height: 2px;
    background: linear-gradient(90deg, rgba(227,180,93,0), var(--gold-light) 50%, rgba(227,180,93,0));
  }
  .visit {
    top: 244px;
    font-family: "Montserrat", sans-serif; font-weight: 500;
    font-size: 28px; letter-spacing: 2.5px;
  }
  .sprig { position: absolute; top: 256px; width: 62px; height: 12px; border-radius: 6px;
    background: linear-gradient(90deg, rgba(227,180,93,0), var(--gold)); }
  .sprig--left { left: 168px; }
  .sprig--right { right: 168px; transform: scaleX(-1); }
  .address {
    top: 286px;
    font-family: "Cinzel", serif; font-weight: 700;
    font-size: 64px; letter-spacing: 1px; line-height: 1.2;
  }

  .features { position: absolute; left: 0; top: 385px; width: 1200px; height: 110px; }
  .feature-icon { position: absolute; }
  .feature-icon--fiber {
    left: 104px; top: 4px; width: 106px; height: 106px; border-radius: 50%;
    background: radial-gradient(circle at 40% 35%, var(--gold-shine), var(--gold) 50%, var(--gold-deep));
  }
  .feature-icon--finance {
    left: 556px; top: 6px; width: 108px; height: 100px; border-radius: 14px;
    background: linear-gradient(180deg, rgba(248,221,142,.9), rgba(168,112,47,.35));
  }
  .feature-text {
    position: absolute; margin: 0;
    font-family: "Montserrat", sans-serif; font-weight: 400;
    font-size: 34px; line-height: 1.32;
  }
  .feature-text--fiber { left: 236px; top: 18px; }
  .feature-text--finance { left: 678px; top: 8px; }
  .feature-text strong { font-weight: 700; }
  .feature-text small { font-size: 26px; }
  .divider { position: absolute; left: 519px; top: 3px; width: 2px; height: 100px;
    background: linear-gradient(180deg, rgba(227,180,93,0), var(--gold), rgba(227,180,93,0)); }

  .tagline {
    top: 541px;
    font-family: "Montserrat", sans-serif; font-weight: 700;
    font-size: 27px; letter-spacing: 2.5px;
  }
  .phone {
    top: 568px;
    font-family: "EB Garamond", serif; font-weight: 700;
    font-size: 138px; letter-spacing: 1px; line-height: 1.1;
  }
</style>
</head>
<body>
<main class="sign">
  <svg class="frame" width="1200" height="800" viewBox="0 0 1200 800" aria-hidden="true">
    <defs>
      <linearGradient id="frameGold" x1="0" y1="0" x2="1" y2="1">
        <stop offset="0" stop-color="#f8dd8e"/>
        <stop offset=".5" stop-color="#c8913f"/>
        <stop offset="1" stop-color="#f3d58c"/>
      </linearGradient>
    </defs>
    <rect x="42" y="24" width="1116" height="752" fill="none" stroke="url(#frameGold)" stroke-width="3"/>
    <rect x="54" y="36" width="1092" height="728" fill="none" stroke="url(#frameGold)" stroke-width="1.5"/>
  </svg>
  <div class="welcome-mask"></div>

  <div class="flourish flourish--tl" role="img" aria-label="Gold leaf flourish"></div>
  <div class="flourish flourish--tr" role="img" aria-label="Gold leaf flourish"></div>
  <div class="flourish flourish--bl" role="img" aria-label="Gold leaf flourish"></div>
  <div class="flourish flourish--br" role="img" aria-label="Gold leaf flourish"></div>

  <p class="line welcome"><span class="gold">WELCOME TO</span></p>
  <h1 class="line community gold">CORWICK MEADOWS</h1>
  <div class="rule"></div>

  <div class="sprig sprig--left" role="img" aria-label="Gold leaf sprig"></div>
  <p class="line visit gold">COME VISIT THE PRD SALES CENTER AT</p>
  <div class="sprig sprig--right" role="img" aria-label="Gold leaf sprig"></div>
  <h2 class="line address gold">745 THISTLEDOWN ROAD</h2>

  <section class="features">
    <div class="feature-icon feature-icon--fiber" role="img" aria-label="Fiber optic cable icon"></div>
    <p class="feature-text feature-text--fiber gold">High Speed<br>Fiber Internet</p>
    <div class="divider"></div>
    <div class="feature-icon feature-icon--finance" role="img" aria-label="Hand holding a dollar coin icon"></div>
    <p class="feature-text feature-text--finance gold">Land financing starting<br>at <strong>$299</strong> <small>(No credit checks)</small></p>
  </section>

  <p class="line tagline gold">LET US BUILD YOUR DREAM HOME!</p>
  <p class="line phone gold">555-284-7390</p>
</main>
</body>
</html>
```